New website for Pollard Law Firm at www.keepwinning-example.com

We are a professional law firm located in the Nashville, Tennessee USA area. We focus on personal injury law. We are looking for a slick new website that is user friendly for updating with new blogs, videos, etc. The primary colors should be red, black, and white. It should load extremely fast and have a good mobile component. The pages for the design will include a home page, about us, news, contact us, and practice page. The practice page will be copied for all the practice areas including motor vehicle accidents, slip and fall accidents, dog bites, etc. We have included an image which we would like to include in the new site which shows the color scheme The image is called banner-Car Wreck. The new website should NOT have gavels, court houses, law books, scales or the typical images for a law firm.

Target Market(s)

People in Tennessee involved in accidents

Industry/Entity Type

Legal services, law firm

Coding

Coded - Design and coding required

Number of Pages Required

5+ page

Font styles to use
Serif

Colors
EB3D1F
EC4F4E
F09395
F8D3D4
FCEDEE

Requirements
Should not have
• Gavels, columns, scales, law related images

```html
<!DOCTYPE html>
<html lang="en">
<head>
<meta charset="utf-8">
<title>Pollard Law Firm — Don't lose what's legally yours</title>
<link rel="stylesheet" href="https://fonts.googleapis.com/css2?family=Lora:ital,wght@0,400;0,500;1,400&family=Open+Sans:wght@400;600;700&display=swap">
<style>
:root{
  --ink:#0e0f13;
  --ink-2:#15171c;
  --panel:#1b1d23;
  --red:#c8232c;
  --red-bright:#e0333a;
  --white:#ffffff;
  --text:#2b2d33;
  --muted:#6c6f78;
  --line:#d9dbe0;
  --soft:#f3f4f7;
  --field:#e3e5ea;
  --serif:'Lora', Georgia, serif;
  --sans:'Open Sans', Arial, sans-serif;
}
*{box-sizing:border-box;margin:0;padding:0}
html,body{width:1200px;height:5172px;overflow:hidden}
body{position:relative;background:var(--white);font-family:var(--sans);color:var(--text)}
.abs{position:absolute}
a{color:inherit;text-decoration:none}

/* Header + hero */
.hero{position:absolute;left:0;top:0;width:1200px;height:1348px;background:linear-gradient(180deg,#111216 0%,#0d0e12 100%)}
.hero-photo{position:absolute;left:590px;top:120px;width:610px;height:542px;
  background:radial-gradient(ellipse at 55% 45%,#b3202a 0%,#6e1419 35%,#2a1418 60%,#111216 80%)}
.brand-panel{position:absolute;left:0;top:0;width:206px;height:176px;background:var(--panel)}
.side-rail{position:absolute;left:0;top:176px;width:96px;height:486px;background:var(--ink-2)}
.brand{position:absolute;left:36px;top:34px;font-family:var(--serif);font-size:25px;color:var(--red-bright);letter-spacing:.5px}
.slide-count{position:absolute;left:42px;top:108px;font-family:var(--sans);font-weight:700;font-size:34px;color:var(--red-bright)}
.slide-count small{font-size:11px;color:#b8bac0;vertical-align:top;margin-left:4px;font-weight:400}
.rail-link{position:absolute;left:40px;font-size:9px;letter-spacing:2px;color:#6a6c74;transform:rotate(-90deg);transform-origin:left top;text-transform:uppercase}
.top-phone{position:absolute;left:238px;top:36px;display:flex;align-items:center;gap:10px;font-size:11px;font-weight:600;color:#e8e9ec}
.top-phone .dot{width:20px;height:20px;border-radius:50%;background:#25272d;display:flex;align-items:center;justify-content:center}
.main-nav{position:absolute;top:39px;left:0;width:100%;font-size:10px;font-weight:600;letter-spacing:.6px;color:#e8e9ec;text-transform:uppercase}
.main-nav a{position:absolute}
.eyebrow{position:absolute;left:166px;top:295px;font-size:10px;font-weight:700;letter-spacing:2.6px;color:var(--red-bright);text-transform:uppercase}
.hero-title{position:absolute;left:164px;top:326px;font-family:var(--serif);font-weight:400;font-size:54px;line-height:64px;color:var(--white)}
.hero-title em{font-style:italic}
.btn{display:flex;align-items:center;justify-content:center;font-size:12px;font-weight:600;color:var(--white);background:var(--red)}
.hero-cta{position:absolute;left:168px;top:492px;width:184px;height:44px}
.partners{position:absolute;left:0;top:690px;width:1200px;height:100px}
.partner-badge{position:absolute;top:22px;height:44px;border-radius:4px;background:#23252b}
.hero-rule{position:absolute;left:144px;top:822px;width:908px;height:1px;background:#24262c}
.trial-title{position:absolute;left:0;top:894px;width:1200px;text-align:center;font-family:var(--serif);font-size:42px;color:var(--white)}
.trial-copy{position:absolute;left:236px;top:978px;width:712px;text-align:center;font-size:11.4px;line-height:25.6px;color:#e4e5e8}
.btn-outline{position:absolute;left:510px;top:1218px;width:176px;height:46px;border:1.5px solid var(--red);color:var(--red-bright);font-size:12px;font-weight:600;display:flex;align-items:center;justify-content:center}

/* Section headings */
.section-title{position:absolute;font-family:var(--serif);font-weight:400;font-size:44px;color:#15171c}
.title-line{position:absolute;height:2px;background:var(--red)}
.lead{position:absolute;font-size:12.5px;line-height:26px;color:#3a3c42}

/* Practice areas */
.practice-card{position:absolute;width:278px;height:326px;overflow:hidden}
.practice-card .label{position:absolute;left:22px;bottom:28px;font-size:19px;font-weight:600;color:var(--white)}
.practice-more{position:absolute;left:506px;top:2356px;width:186px;height:44px}
.divider{position:absolute;left:156px;top:2494px;width:886px;height:1px;background:var(--line)}

/* Videos */
.btn-ghost{position:absolute;display:flex;align-items:center;justify-content:center;border:1px solid var(--line);font-size:12px;font-weight:600;color:var(--red)}
.video-card{position:absolute;overflow:hidden}
.video-card .caption{position:absolute;left:30px;bottom:22px;width:520px;font-size:12.5px;line-height:24px;color:var(--white)}
.play{position:absolute;width:60px;height:60px;border-radius:50%;background:var(--white);display:flex;align-items:center;justify-content:center}
.dots{position:absolute;left:564px;top:3104px;display:flex;gap:6px;align-items:center}
.dots span{width:7px;height:7px;border-radius:50%;background:#cfd1d6}
.dots .on{width:22px;border-radius:4px;background:var(--red)}

/* Quote + news band */
.news-band{position:absolute;left:0;top:3336px;width:1200px;height:744px;background:var(--soft)}
.quote{position:absolute;left:156px;top:3204px;width:886px;height:256px;background:var(--red);text-align:center;color:var(--white)}
.quote p{position:absolute;left:90px;top:50px;width:706px;font-family:var(--serif);font-size:23px;line-height:38px}
.quote cite{position:absolute;left:0;top:195px;width:100%;font-style:normal;font-size:9.5px;font-weight:700;letter-spacing:2.4px}
.news-photo{position:absolute;width:278px;height:218px}
.news-date{position:absolute;font-size:9px;font-weight:700;letter-spacing:2px;color:#a3a6ad;text-transform:uppercase}
.news-title{position:absolute;width:278px;font-family:var(--serif);font-size:19px;line-height:28px;color:#24262c}
.news-body{position:absolute;width:278px;font-size:11px;line-height:22.4px;color:#4a4c52}
.read-more{position:absolute;font-size:10px;font-weight:700;letter-spacing:1.6px;color:var(--red);text-decoration:underline;text-underline-offset:3px}

/* Contact */
.field-label{position:absolute;font-size:10.5px;color:#4a4c52}
.field{position:absolute;height:46px;border:1px solid var(--field);background:var(--white)}
.field.area{height:116px}
.field.area span{position:absolute;left:14px;top:18px;font-size:11px;color:#7a7d85}
.send{position:absolute;left:156px;top:4612px;width:184px;height:46px}
.contact-intro{position:absolute;left:762px;top:4286px;font-size:18px;line-height:28px;color:#24262c}
.contact-item{position:absolute;left:762px}
.contact-item h4{margin-left:26px;font-size:10px;font-weight:700;letter-spacing:1.4px;color:var(--red)}
.contact-item p{margin-left:26px;margin-top:6px;font-size:10.5px;line-height:21px;color:#4a4c52}
.contact-item svg{position:absolute;left:0;top:1px}

/* Footer */
.footer{position:absolute;left:0;top:4754px;width:1200px;height:418px;background:var(--ink)}
.footer-brand{position:absolute;left:156px;top:118px;font-family:var(--serif);font-size:25px;color:var(--red-bright)}
.footer-text{position:absolute;font-size:10.5px;line-height:21px;color:#d9dade}
.footer-head{position:absolute;font-size:11px;font-weight:600;color:var(--white)}
.footer-list{position:absolute;list-style:none;font-size:10.5px;line-height:27px;color:#d9dade}
.social-list li{display:flex;align-items:center;gap:12px;height:34px}
.social-list .dot{width:18px;height:18px;border-radius:50%;background:#26282e}
.footer-line{position:absolute;display:flex;align-items:center;gap:12px;font-size:10.5px;color:#d9dade}
.copyright{position:absolute;left:0;top:340px;width:100%;text-align:center;font-size:9.5px;color:#d9dade}
.copyright b{font-weight:400;color:var(--red-bright)}
.footer-stripe{position:absolute;left:0;bottom:0;width:100%;height:6px;background:var(--red)}
</style>
</head>
<body>

<!-- Hero -->
<section class="hero">
  <div class="hero-photo" role="img" aria-label="Photo of a red car shattering in a collision, glass flying"></div>
  <div class="brand-panel">
    <div class="brand">Pollard Law Firm</div>
    <div class="slide-count">01<small>/04</small></div>
  </div>
  <div class="side-rail">
    <span class="rail-link" style="top:210px">Linkwork</span>
    <span class="rail-link" style="top:320px">Chirper</span>
    <span class="rail-link" style="top:440px">Friendbook</span>
  </div>
  <div class="top-phone">
    <span class="dot"><svg width="10" height="10" viewBox="0 0 24 24"><path fill="#e8e9ec" d="M6.6 10.8a15 15 0 0 0 6.6 6.6l2.2-2.2c.3-.3.7-.4 1-.2 1.1.4 2.3.6 3.6.6.6 0 1 .4 1 1V20c0 .6-.4 1-1 1A17 17 0 0 1 3 4c0-.6.4-1 1-1h3.5c.6 0 1 .4 1 1 0 1.3.2 2.5.6 3.6.1.3 0 .7-.2 1z"/></svg></span>
    (615) 555-0140
  </div>
  <nav class="main-nav">
    <a style="left:644px">Home</a>
    <a style="left:722px">Practices</a>
    <a style="left:820px">Our team</a>
    <a style="left:918px">News</a>
    <a style="left:990px">Contact</a>
  </nav>
  <div class="eyebrow">Pollard Law Firm PLLC</div>
  <h1 class="hero-title">Don’t lose what’s<br><em>legally</em> yours</h1>
  <a class="btn hero-cta">Contact us</a>

  <div class="partners" aria-label="Partner banks">
    <div class="partner-badge" style="left:136px;width:190px"></div>
    <div class="partner-badge" style="left:364px;width:168px"></div>
    <div class="partner-badge" style="left:576px;width:66px;top:10px;height:68px"></div>
    <div class="partner-badge" style="left:684px;width:136px"></div>
    <div class="partner-badge" style="left:874px;width:192px"></div>
  </div>
  <div class="hero-rule"></div>

  <h2 class="trial-title">Trial Lawyers...</h2>
  <p class="trial-copy">WE ARE TRIAL LAWYERS AND WE ARE PROUD OF IT! &nbsp;There are many law firms in Tennessee who claim to be trial lawyers, but their attorneys have never seen a courtroom. &nbsp;We have tried hundreds of cases to verdict and we have helped thousands of people in the Tennessee courts. &nbsp;We fight against billion dollar insurance companies, billion dollar corporations, and the State of Tennessee..and we win!It is very hard not to take each case personally. &nbsp;Our clients include victims of personal injury who did not ask for the pain from a car wreck; professionals who are trying to provide for their family and save their license; and parents falsely accused in a child custody proceeding. &nbsp;The majority of our clients are referred by other attorneys because they need our specialized expertise. &nbsp;Given what is at stake, we take each client’s matter personally and try to work on each case every day in order to bring justice to our clients.</p>
  <a class="btn-outline">Meet our team</a>
</section>

<!-- Practice areas -->
<div class="title-line" style="left:324px;top:1474px;width:66px"></div>
<h2 class="section-title" style="left:410px;top:1440px">Our Practice Areas</h2>
<div class="title-line" style="left:808px;top:1474px;width:66px"></div>
<p class="lead" style="left:256px;top:1526px;width:688px;text-align:center">We are the only law firm in Tennessee who has a website like www.keepwinning-example.com. &nbsp;We strive to help our clients and do everything we can to make sure that they don’t lose the money that is owed, don’t lose their license, and don’t lose their family.</p>

<div class="practice-card" style="left:156px;top:1638px;background:linear-gradient(160deg,#b94a3e,#6d5a55 55%,#3a3535)" role="img" aria-label="Photo of paramedics treating an injured person"><span class="label">Personal injury</span></div>
<div class="practice-card" style="left:460px;top:1638px;background:linear-gradient(160deg,#9ea2a8,#5d6168 55%,#2e3035)" role="img" aria-label="Photo of a crashed car front"><span class="label">Motor accidents</span></div>
<div class="practice-card" style="left:764px;top:1638px;background:linear-gradient(160deg,#d7d2cc,#8a6a58 55%,#4a3a33)" role="img" aria-label="Photo of a child with a parent"><span class="label">Child custody</span></div>
<div class="practice-card" style="left:156px;top:1988px;background:linear-gradient(170deg,#6f8560,#8b8e8a 50%,#4e4e50)" role="img" aria-label="Photo of a skateboarder falling"><span class="label">Slip and fall accidents</span></div>
<div class="practice-card" style="left:460px;top:1988px;background:linear-gradient(160deg,#e6e7ea,#8c8f97 55%,#2f3441)" role="img" aria-label="Photo of a professional in a meeting"><span class="label">Professional licenses</span></div>
<div class="practice-card" style="left:764px;top:1988px;background:linear-gradient(160deg,#141414,#2e2a27 55%,#161514)" role="img" aria-label="Photo of a barking dog on a dark background"><span class="label">Dog bites</span></div>
<a class="btn practice-more">View all practice areas</a>

<div class="divider"></div>

<!-- Featured videos -->
<h2 class="section-title" style="left:156px;top:2566px">Featured videos</h2>
<div class="title-line" style="left:498px;top:2604px;width:66px"></div>
<p class="lead" style="left:154px;top:2634px;width:620px">We strive to help our clients and do everything we can to make sure that they don’t lose the money that is owed, don’t lose their license, and don’t lose their family.</p>
<a class="btn-ghost" style="left:882px;top:2636px;width:162px;height:46px">All videos</a>

<div class="video-card" style="left:0;top:2732px;width:112px;height:332px;background:linear-gradient(160deg,#6b6f78,#2c2e34)" role="img" aria-label="Video still of a meeting"></div>
<div class="video-card" style="left:142px;top:2732px;width:674px;height:332px;background:linear-gradient(160deg,#c9ccd1,#8d9098 45%,#4a4c52);box-shadow:0 14px 30px rgba(0,0,0,.18)" role="img" aria-label="Video still of lawyers meeting with clients at a table">
  <div class="play" style="left:306px;top:152px"><svg width="18" height="20" viewBox="0 0 18 20"><path d="M2 1l15 9-15 9z" fill="#c8232c"/></svg></div>
  <p class="caption">Integer iaculis pellentesque odio vel tincidunt. Nam efficitur nibh pharetra nunc consequat, et iaculis nunc faucibus. Fusce gravida sagittis malesuada.</p>
</div>
<div class="video-card" style="left:848px;top:2732px;width:352px;height:332px;background:linear-gradient(160deg,#d8d9dc,#8f7670 50%,#4a3d3d)" role="img" aria-label="Video still of a family meeting with a lawyer">
  <div class="play" style="left:242px;top:152px;background:rgba(255,255,255,.35)"><svg width="18" height="20" viewBox="0 0 18 20"><path d="M2 1l15 9-15 9z" fill="#ffffff"/></svg></div>
  <p class="caption" style="left:30px;width:520px">Integer iaculis pellentesque odio vel tincidunt. Nam efficitur nibh pharetra nunc consequat, et iaculis nunc faucibus. Fusce gravida sagittis malesuada.</p>
</div>
<div class="dots"><span></span><span class="on"></span><span></span><span></span></div>

<!-- Quote + news -->
<div class="news-band"></div>
<blockquote class="quote">
  <p>“Speak up for those who cannot speak for themselves, for the rights of all who are destitute. Speak up and judge fairly; defend the rights of the poor and needy.”</p>
  <cite>— PROVERBS 31:8-9</cite>
</blockquote>

<div class="title-line" style="left:382px;top:3560px;width:66px"></div>
<h2 class="section-title" style="left:476px;top:3520px">Latest News</h2>
<div class="title-line" style="left:746px;top:3560px;width:66px"></div>

<div class="news-photo" style="left:156px;top:3632px;background:linear-gradient(160deg,#d5d6d9,#8b7a74 50%,#4a3c3c)" role="img" aria-label="Photo of a family with a lawyer"></div>
<div class="news-date" style="left:156px;top:3870px">29 September, 2020</div>
<h3 class="news-title" style="left:156px;top:3890px">Maecenas sed elit pulvinar aliquam erat eget</h3>
<a class="read-more" style="left:156px;top:3968px">READ MORE</a>

<div class="news-date" style="left:460px;top:3646px">29 September, 2020</div>
<h3 class="news-title" style="left:460px;top:3666px">Pollard Obtains Jury Verdict of 61 x Medical Bills</h3>
<p class="news-body" style="left:460px;top:3736px">In 2016, a client was traveling down a road and stopped in traffic when she was hit by another driver in the rear end. &nbsp;Although she thought she was okay, she immediately began to hear a ringing in her ear. &nbsp;Prior to the accident, she had tinnitus and it was liveable however, this was unbearable. &nbsp;She believed it would go away and tried to do everything she could to ignore it for the next few weeks.</p>
<a class="read-more" style="left:460px;top:3968px">READ MORE</a>

<div class="news-photo" style="left:764px;top:3624px;background:linear-gradient(160deg,#a2a6ac,#5e6168 50%,#2b2d32)" role="img" aria-label="Photo of a crashed car"></div>
<div class="news-date" style="left:764px;top:3862px">29 September, 2020</div>
<h3 class="news-title" style="left:764px;top:3882px">Maecenas sed elit pulvinar aliquam erat eget</h3>
<a class="read-more" style="left:764px;top:3968px">READ MORE</a>

<!-- Contact -->
<h2 class="section-title" style="left:156px;top:4164px">Get in touch</h2>
<div class="title-line" style="left:430px;top:4204px;width:66px"></div>

<label class="field-label" style="left:156px;top:4256px">First name</label>
<div class="field" style="left:156px;top:4280px;width:254px"></div>
<label class="field-label" style="left:432px;top:4256px">Last name</label>
<div class="field" style="left:432px;top:4280px;width:254px"></div>
<label class="field-label" style="left:156px;top:4344px">Email address</label>
<div class="field" style="left:156px;top:4368px;width:254px"></div>
<label class="field-label" style="left:432px;top:4344px">Phone number</label>
<div class="field" style="left:432px;top:4368px;width:254px"></div>
<label class="field-label" style="left:156px;top:4438px">How can we help you ?</label>
<div class="field area" style="left:156px;top:4462px;width:530px"><span>Your message</span></div>
<a class="btn send">Send message</a>

<p class="contact-intro">Don’t hesitate to contact<br>us for any information.</p>
<div class="contact-item" style="top:4350px">
  <svg width="12" height="10" viewBox="0 0 12 10"><rect x="0.5" y="0.5" width="11" height="9" fill="#c8232c"/><path d="M1 1l5 4 5-4" stroke="#fff" fill="none"/></svg>
  <h4>EMAIL</h4><p>office@pollardlawfirm-example.com</p>
</div>
<div class="contact-item" style="top:4406px">
  <svg width="12" height="12" viewBox="0 0 24 24"><path fill="#c8232c" d="M6.6 10.8a15 15 0 0 0 6.6 6.6l2.2-2.2c.3-.3.7-.4 1-.2 1.1.4 2.3.6 3.6.6.6 0 1 .4 1 1V20c0 .6-.4 1-1 1A17 17 0 0 1 3 4c0-.6.4-1 1-1h3.5c.6 0 1 .4 1 1 0 1.3.2 2.5.6 3.6.1.3 0 .7-.2 1z"/></svg>
  <h4>PHONE</h4><p>(615) 555-0172<br>(615) 555-0173 (fax)</p>
</div>
<div class="contact-item" style="top:4496px">
  <svg width="10" height="13" viewBox="0 0 10 13"><path fill="#c8232c" d="M5 0a5 5 0 0 1 5 5c0 3.5-5 8-5 8S0 8.5 0 5a5 5 0 0 1 5-5zm0 3a2 2 0 1 0 0 4 2 2 0 0 0 0-4z"/></svg>
  <h4>ADDRESS</h4><p>1820 Birchwood Lane<br>Suite 210, Maple Court<br>Franklin, TN 37064</p>
</div>

<!-- Footer -->
<footer class="footer">
  <div class="footer-brand">Pollard Law Firm</div>
  <p class="footer-text" style="left:158px;top:174px">1820 Birchwood Lane<br>Suite 210. Franklin, TN 37064</p>
  <div class="footer-line" style="left:160px;top:230px">
    <svg width="12" height="10" viewBox="0 0 12 10"><rect x="0.5" y="0.5" width="11" height="9" fill="#d9dade"/><path d="M1 1l5 4 5-4" stroke="#0e0f13" fill="none"/></svg>
    office@pollardlawfirm-example.com
  </div>
  <div class="footer-line" style="left:160px;top:264px">
    <svg width="12" height="12" viewBox="0 0 24 24"><path fill="#d9dade" d="M6.6 10.8a15 15 0 0 0 6.6 6.6l2.2-2.2c.3-.3.7-.4 1-.2 1.1.4 2.3.6 3.6.6.6 0 1 .4 1 1V20c0 .6-.4 1-1 1A17 17 0 0 1 3 4c0-.6.4-1 1-1h3.5c.6 0 1 .4 1 1 0 1.3.2 2.5.6 3.6.1.3 0 .7-.2 1z"/></svg>
    (615) 555-0140
  </div>

  <h4 class="footer-head" style="left:480px;top:110px">Quick links</h4>
  <ul class="footer-list" style="left:482px;top:146px"><li>Home</li><li>Practice &nbsp;area</li><li>Our team</li><li>News</li><li>contact</li></ul>

  <h4 class="footer-head" style="left:670px;top:110px">Support</h4>
  <ul class="footer-list" style="left:672px;top:146px"><li>Terms and conditions</li><li>Privacy policy</li><li>Help</li><li>Contact us</li></ul>

  <h4 class="footer-head" style="left:920px;top:110px">Get social</h4>
  <ul class="footer-list social-list" style="left:920px;top:140px"><li><span class="dot"></span>Friendbook</li><li><span class="dot"></span>Chirper</li><li><span class="dot"></span>Linkwork</li><li><span class="dot"></span>Snapgram</li></ul>

  <p class="copyright">© 2021 <b>Pollard Law Firm, PLLC</b> . all rights reserved</p>
  <div class="footer-stripe"></div>
</footer>

</body>
</html>
```